KVT Business Cards

We require business cards for our business. We would like a matte black back to the card, with our logo centred in the middle. The front side of the card is open to design.

Target Market(s)

Clients looking for legal services (professional)

Industry/Entity Type

Legal

Contact Information for Business Card

Boris Telemark
Partner
Mobile: 0438 715 642
Email: boris@kvtlaw.co
Website: www.kvtlaw.co
Level 3, 118 Wexbury Street
Sydney NSW 2000

Font styles to use
Other font styles liked:
• Avenir

Colors
f04a50
ffffff
1b1b1b

Requirements
Must have
• Black back with logo included in the centre of the card.
• Our font is Avenir.

```html
<!DOCTYPE html>
<html lang="en">
<head>
<meta charset="utf-8">
<title>KVT Business Cards</title>
<link rel="stylesheet" href="https://fonts.googleapis.com/css2?family=Nunito+Sans:wght@400;700;800&display=swap">
<style>
  :root {
    --ground: #3a3a3d;
    --brand: #c9204a;
    --brand-light: #d42f57;
    --ink: #1b1b1b;
    --matte: #1b1b1b;
    --paper: #ffffff;
    --muted: rgba(255,255,255,0.85);
    --shadow: rgba(0,0,0,0.5);
  }
  * { box-sizing: border-box; margin: 0; padding: 0; }
  html, body {
    width: 1200px; height: 892px; overflow: hidden;
    background: var(--ground);
    font-family: "Nunito Sans", "Avenir", sans-serif;
  }
  .stage { position: relative; width: 1200px; height: 892px; }
  .card {
    position: absolute; width: 600px; height: 343px;
    box-shadow: 0 18px 40px var(--shadow);
    overflow: hidden;
  }

  /* Back: matte black with centred name */
  .card--back {
    left: 80px; top: 70px;
    background: var(--matte);
    color: var(--paper);
  }
  .brand-mark {
    position: absolute; left: 0; right: 0; top: 0; bottom: 0;
    display: flex; justify-content: center; align-items: center; gap: 14px;
  }
  .brand-mark__square { width: 20px; height: 20px; background: var(--brand); }
  .brand-mark__name { font-size: 64px; font-weight: 800; letter-spacing: 4px; line-height: 1; }
  .brand-url {
    position: absolute; left: 0; right: 0; bottom: 40px;
    text-align: center; font-size: 14px; letter-spacing: 11px; text-transform: uppercase;
    color: var(--muted);
  }

  /* Front: contact side */
  .card--front {
    left: 520px; top: 480px;
    display: flex;
  }
  .front-logo {
    width: 262px; background: var(--paper);
    display: flex; align-items: center; justify-content: center; gap: 12px;
  }
  .front-logo__square { width: 16px; height: 16px; background: var(--brand); flex: none; }
  .front-logo__name {
    color: var(--ink); font-size: 20px; font-weight: 700; line-height: 1.05;
    text-transform: uppercase; letter-spacing: 0.5px;
  }
  .divider-band { width: 20px; background: var(--ink); }
  .contact-details {
    flex: 1; padding: 34px 30px;
    background: linear-gradient(135deg, var(--brand-light), var(--brand));
    color: var(--paper); position: relative;
  }
  .person__name { font-size: 22px; font-weight: 800; }
  .person__role { font-size: 14px; margin-top: 2px; }
  .address { position: absolute; left: 30px; top: 170px; font-size: 14px; line-height: 1.35; }
  .contact-list { position: absolute; left: 30px; top: 222px; list-style: none; font-size: 14px; line-height: 1.45; }
  .contact-list li { display: flex; align-items: center; gap: 9px; }
  .contact-list svg { width: 13px; height: 13px; flex: none; }
</style>
</head>
<body>
<main class="stage">

  <section class="card card--back" aria-label="Business card, back">
    <div class="brand-mark">
      <span class="brand-mark__square"></span>
      <span class="brand-mark__name">KVT</span>
    </div>
    <p class="brand-url">www.kvtlaw.co</p>
  </section>

  <section class="card card--front" aria-label="Business card, front">
    <div class="front-logo">
      <span class="front-logo__square"></span>
      <span class="front-logo__name">Kessler<br>Vane<br>Telemark</span>
    </div>
    <div class="divider-band"></div>
    <div class="contact-details">
      <h1 class="person__name">Boris Telemark</h1>
      <p class="person__role">Partner</p>
      <p class="address">Level 3, 118 Wexbury Street<br>Sydney NSW 2000</p>
      <ul class="contact-list">
        <li>
          <svg viewBox="0 0 12 12" aria-hidden="true"><rect x="3" y="0.5" width="6" height="11" rx="1" fill="none" stroke="#fff" stroke-width="1.3"/><circle cx="6" cy="9.5" r="0.8" fill="#fff"/></svg>
          0438 715 642
        </li>
        <li>
          <svg viewBox="0 0 12 12" aria-hidden="true"><rect x="0.5" y="2.5" width="11" height="7" fill="#fff"/><path d="M0.5 2.5 L6 6.5 L11.5 2.5" fill="none" stroke="#c9204a" stroke-width="1"/></svg>
          boris@kvtlaw.co
        </li>
        <li>
          <svg viewBox="0 0 12 12" aria-hidden="true"><circle cx="6" cy="6" r="5.5" fill="#fff"/><path d="M0.5 6 H11.5 M6 0.5 C3 3.5 3 8.5 6 11.5 M6 0.5 C9 3.5 9 8.5 6 11.5" fill="none" stroke="#c9204a" stroke-width="0.9"/></svg>
          www.kvtlaw.co
        </li>
      </ul>
    </div>
  </section>

</main>
</body>
</html>
```